Harbor Lane Wick's Seasonal promotions!

We would like two banners for our website, one for Spring and one for Mothers Day. On the Spring Banner we would like our candles to be featured with a beautiful spring background (flowers, or a garden, etc as long as it's spring)- it does not have to be all of them it could just be one of the four candles I posted, be creative! We would like to include our our Spring deals which is 30% OFF our Spring Collection and free shipping when you purchase $50 or more. Instead of Spring deals put something catchy like "Hello Spring!" or "Spring is here.."
For the mothers day banner we would like a banner with our Everlasting Glow candle in it (the large ones with the black label). We leave the creativity to you. We would like to include in this one the deals: 30% OFF and a free 8 ounce air freshener when you purchase $75 dollars or more (a $15 dollar value). As far as wording goes, we would like something pretty and sweet in regards to Mother's Day. We leave the creativity to you. Just note that we want our banners to be elegant and to the point. Please note these banners are separate and the deals are separate.
Updates
Please note: These banners will be on our website, they do not require our logo.Banner size: 314 height x 783 width Added Tuesday, April 14, 2015
Having said that I did upload our logo in case you would like to use it in the banner, it's not necessary but I leave the creativity up to you. Added Tuesday, April 14, 2015

```html
<!DOCTYPE html>
<html lang="en">
<head>
<meta charset="UTF-8">
<title>Harbor Lane Wick – Spring is here</title>
<link rel="stylesheet" href="https://fonts.googleapis.com/css2?family=Anton&family=Overlock:wght@700;900&display=swap">
<style>
  :root {
    --page: #ffffff;
    --sky-top: #0a9cd6;
    --sky-mid: #52b8e6;
    --sky-glow: #d6eef9;
    --cloud: #f4f7f9;
    --meadow-green: #4f9a3a;
    --meadow-light: #a9d58a;
    --hill-dark: #3e8a1f;
    --hill-light: #9fd14e;
    --candle-dark: #1d1d1d;
    --candle-light: #f2f2f2;
    --deal-red: #e3171c;
    --text-white: #ffffff;
    --arrow: #cfe9f7;
  }
  html, body {
    margin: 0;
    width: 1200px;
    height: 900px;
    overflow: hidden;
    background: var(--page);
  }
  .canvas {
    position: relative;
    width: 1200px;
    height: 900px;
  }
  .banner {
    position: absolute;
    left: 207px;
    top: 295px;
    width: 783px;
    height: 314px;
    overflow: hidden;
    background:
      radial-gradient(ellipse 260px 230px at 370px 150px, var(--sky-glow) 0%, rgba(214,238,249,0.4) 45%, rgba(214,238,249,0) 100%),
      linear-gradient(180deg, var(--sky-top) 0%, var(--sky-mid) 55%, #9ed6f0 100%);
    font-family: "Overlock", sans-serif;
  }
  .art { position: absolute; }
  .sky-haze-left, .sky-haze-right {
    top: -60px; width: 240px; height: 150px;
  }
  .sky-haze-left {
    left: -70px;
    background: radial-gradient(ellipse 50% 50% at 50% 50%, rgba(244,247,249,0.95) 0%, rgba(244,247,249,0.6) 45%, rgba(244,247,249,0) 100%);
  }
  .sky-haze-right {
    left: 613px;
    background: radial-gradient(ellipse 50% 50% at 50% 50%, rgba(244,247,249,0.95) 0%, rgba(244,247,249,0.6) 45%, rgba(244,247,249,0) 100%);
  }
  .meadow {
    left: 0; top: 150px; width: 783px; height: 164px;
    background:
      linear-gradient(180deg, rgba(169,213,138,0) 0%, rgba(169,213,138,0.8) 40%, var(--meadow-green) 100%);
    -webkit-mask-image: linear-gradient(90deg, #000 0%, #000 24%, transparent 40%, transparent 62%, #000 76%, #000 100%);
    mask-image: linear-gradient(90deg, #000 0%, #000 24%, transparent 40%, transparent 62%, #000 76%, #000 100%);
  }
  .hill {
    left: 255px; top: 268px; width: 230px; height: 120px;
    border-radius: 50%;
    background: radial-gradient(ellipse at 50% 20%, var(--hill-light) 0%, var(--hill-dark) 70%);
  }
  .candle-set {
    left: 290px; top: 110px; width: 145px; height: 180px;
    border-radius: 14px 14px 6px 6px;
    background: linear-gradient(90deg, var(--candle-dark) 0%, var(--candle-dark) 45%, var(--candle-light) 46%, #dcdcdc 100%);
  }
  .arrows { position: absolute; left: 0; top: 0; }
  .headline {
    position: absolute;
    left: 297px; top: 18px;
    margin: 0;
    white-space: nowrap;
    font-weight: 700;
    color: var(--text-white);
  }
  .headline-season {
    font-size: 40px;
    background: linear-gradient(90deg, #f7f08a 0%, #9fe6ff 30%, #c9a6f5 55%, #f5a0b8 80%, #f7c28a 100%);
    -webkit-background-clip: text;
    background-clip: text;
    color: transparent;
  }
  .headline-tail { font-size: 21px; margin-left: 10px; }
  .headline-rule {
    position: absolute; left: 315px; top: 73px; width: 155px; height: 2px;
    background: linear-gradient(90deg, rgba(255,255,255,0), #ffffff 50%, rgba(255,255,255,0));
  }
  .deal-number {
    position: absolute;
    font-family: "Anton", sans-serif;
    color: var(--deal-red);
    line-height: 1;
  }
  .discount-value { left: 13px; top: 90px; font-size: 70px; }
  .discount-percent { left: 89px; top: 88px; font-size: 40px; }
  .discount-off { left: 89px; top: 124px; font-size: 29px; }
  .deal-copy {
    position: absolute;
    margin: 0;
    font-size: 23px;
    line-height: 21px;
    font-weight: 900;
    color: var(--text-white);
    white-space: nowrap;
  }
  .discount-copy { left: 136px; top: 91px; }
  .shipping-copy { right: 141px; top: 91px; text-align: right; }
  .shipping-value { left: 645px; top: 90px; font-size: 70px; }
  .shipping-currency { left: 728px; top: 84px; font-size: 46px; }
  .shipping-more { left: 720px; top: 137px; font-size: 17px; }
</style>
</head>
<body>
<div class="canvas">
  <section class="banner" aria-label="Harbor Lane Wick spring promotion">
    <div class="art sky-haze-left" role="img" aria-label="Soft white cloud in the upper left sky"></div>
    <div class="art sky-haze-right" role="img" aria-label="Soft white cloud in the upper right sky"></div>

    <svg class="arrows" width="783" height="314" viewBox="0 0 783 314" aria-hidden="true">
      <g fill="none" stroke="var(--arrow)" stroke-width="2" stroke-linecap="round">
        <path d="M288 38 C240 18 185 22 168 68"/>
        <path d="M161 60 L168 70 L175 60"/>
        <path d="M494 38 C542 18 597 22 612 68"/>
        <path d="M605 60 L612 70 L619 60"/>
      </g>
    </svg>

    <h1 class="headline"><span class="headline-season">Spring</span><span class="headline-tail">is here..</span></h1>
    <div class="headline-rule"></div>

    <div class="art meadow" role="img" aria-label="Meadows of wildflowers, poppies and cornflowers with tall grass on both sides"></div>
    <div class="art hill" role="img" aria-label="Green grassy hill"></div>
    <div class="art candle-set" role="img" aria-label="Everlasting Glow candle in a black gift tube beside a white jar candle and a Harbor Lane Wick tin"></div>

    <span class="deal-number discount-value">30</span>
    <span class="deal-number discount-percent">%</span>
    <span class="deal-number discount-off">OFF</span>
    <p class="deal-copy discount-copy">In our<br>Spring<br>Collection</p>

    <p class="deal-copy shipping-copy">Free shipping<br>when you<br>purchase</p>
    <span class="deal-number shipping-value">50</span>
    <span class="deal-number shipping-currency">$</span>
    <span class="deal-number shipping-more">or more</span>
  </section>
</div>
</body>
</html>
```